Law Firm Banner Ads

Hi, I am an account manager for an Ad Agency that is looking for new Banner ads for a client of ours, The Brackwell Law Firm. We would like new ads for their Display Campaigns. The Law Firm Specializes in Criminal Defense, DUIs and a bunch of other stuff. We would like the ads to either list a few key areas or focus on just one area, like DUIs. It is up to you guys on how you would like to do it, and we are open to either approach and simply planning on choosing the one that looks the best and looks like it has the most potential to drive traffic/conversions but we tend to get the best results from designers when we let them have as much freedom as possible. So feel free to make it however you like. We normally ask that the banners match the website because we've seen that congruency helps increase conversion rates, but in this case the website is getting re-made because it is so ugly. If you can match the look of site without making ugly ads, your chances of winning probably do increase, or maybe try to match the mobile site instead of the desktop stie. On the other hand, if you make ads that are super awesome/unique and don't look like the site, your chances of winning can increase as well.
Also feel free to use any text or call to action buttons that you think will look/perform the best. We tend to see that letting people know what they get, rather than what they have to do, tends to work the best.
We are looking for 300x600, 300x50, 300x250, 728x90. Only one size of your choice is required but make as many as you want to showcase the different features of your design.
Animated GIFs and static images are allowed but no Flash.
Size limit is 60kbs.
Some assets are provided but you might want to refer to the web, and desktop/mobile sites for other, more current assets. The ads included are their current ads which are live right now.
Updates
Hi Everybody,
Industry/Entity Type
Law Firm

```html
<!DOCTYPE html>
<html lang="en">
<head>
<meta charset="utf-8">
<title>The Brackwell Law Firm – 300x600 Banner</title>
<link rel="stylesheet" href="https://fonts.googleapis.com/css2?family=Montserrat:wght@500&family=Roboto+Condensed:wght@700&display=swap">
<style>
  :root {
    --stage: #4b5360;
    --paper: #ffffff;
    --ink: #3a2b2b;
    --brand-red: #d13a2c;
    --stone-light: #eef0f2;
    --stone-mid: #cfcac2;
    --sky: #b9cde3;
    --suit-dark: #2b2826;
    --photo-wall: #b9b2ab;
  }
  * { margin: 0; padding: 0; box-sizing: border-box; }
  html, body {
    width: 1200px; height: 1200px; overflow: hidden;
    background: var(--stage);
  }
  .banner {
    position: absolute; left: 375px; top: 150px;
    width: 450px; height: 900px;
    background: var(--paper); overflow: hidden;
  }
  .hero-backdrop {
    position: absolute; left: 0; top: 0; width: 450px; height: 780px;
    background: linear-gradient(160deg, var(--sky) 0%, var(--stone-light) 35%, var(--stone-mid) 70%, #a9a39a 100%);
  }
  .list-panel {
    position: absolute; left: 0; top: 0; width: 405px; height: 282px;
    background: rgba(255,255,255,0.55);
  }
  .practice-list {
    position: absolute; left: 30px; top: 30px; list-style: none;
    font-family: "Montserrat", sans-serif; font-weight: 500;
    font-size: 33px; line-height: 45px; color: var(--ink);
  }
  .practice-list li::before {
    content: "•"; font-size: 22px; display: inline-block;
    width: 30px; vertical-align: 4px;
  }
  .cta-button {
    position: absolute; left: 40px; top: 281px; width: 227px; height: 68px;
    background: var(--brand-red); color: var(--paper);
    font-family: "Montserrat", sans-serif; font-weight: 500; font-size: 30px;
    display: flex; align-items: center; justify-content: center;
    text-decoration: none;
  }
  .phone-bar {
    position: absolute; left: 45px; top: 380px; width: 364px; height: 70px;
    background: var(--paper);
    display: flex; align-items: center; justify-content: center; gap: 12px;
    font-family: "Roboto Condensed", sans-serif; font-weight: 700;
    font-size: 46px; color: var(--brand-red);
  }
  .phone-bar svg { width: 38px; height: 38px; }
  .attorney-photo {
    position: absolute; left: 47px; top: 450px; width: 361px; height: 310px;
    background: linear-gradient(180deg, var(--photo-wall) 0%, #a69e96 55%, var(--suit-dark) 56%, var(--suit-dark) 100%);
  }
  .base-curve {
    position: absolute; left: 0; top: 0; width: 450px; height: 900px;
  }
  .firm-name {
    position: absolute; left: 0; top: 790px; width: 450px;
    text-align: center;
    font-family: "Montserrat", sans-serif; font-weight: 500;
    font-size: 28px; color: var(--brand-red);
  }
</style>
</head>
<body>
  <div class="banner">
    <div class="hero-backdrop" role="img" aria-label="Courthouse columns against a pale sky"></div>
    <div class="list-panel"></div>
    <ul class="practice-list">
      <li>Criminal Defense</li>
      <li>DUI Defense</li>
      <li>White Collar</li>
      <li>Sex Crimes</li>
      <li>Appeals</li>
    </ul>
    <a class="cta-button" href="#">Learn more</a>
    <div class="phone-bar">
      <svg viewBox="0 0 24 24" aria-hidden="true"><path fill="#3a2b2b" d="M6.6 10.8a15.1 15.1 0 0 0 6.6 6.6l2.2-2.2c.3-.3.7-.4 1-.2 1.1.4 2.3.6 3.6.6.6 0 1 .4 1 1V20c0 .6-.4 1-1 1A17 17 0 0 1 3 4c0-.6.4-1 1-1h3.5c.6 0 1 .4 1 1 0 1.3.2 2.5.6 3.6.1.3 0 .7-.2 1z"/></svg>
      <span>480 555 0142</span>
    </div>
    <div class="attorney-photo" role="img" aria-label="Portrait of the two firm attorneys in dark suits"></div>
    <svg class="base-curve" viewBox="0 0 450 900" aria-hidden="true">
      <path d="M0 700 Q 180 770 450 745 L450 752 Q 180 780 0 712 Z" fill="var(--brand-red)"/>
      <path d="M0 712 Q 180 780 450 752 L450 900 L0 900 Z" fill="var(--paper)"/>
    </svg>
    <div class="firm-name">The Brackwell Law Firm</div>
  </div>
</body>
</html>
```